Webdesign für Energieagentur
Zielgruppe
Brixowal richtet sich derzeit als Energieagentur aus.
Neben Strom- und Gastarife für den privaten als auch gewerblichen Wechsel kümmern wir uns um industrielle LED Beleuchtung. Auf der Startseite sollte eine Übersicht der Leistungen* befinden. Durch 'Klick' kommt man auf die Themenseite.
*Leistungen
Strom- Gastarife für Privatkunden
Strom- Gastarife für Gewerbekunden
LED Hallenbeleuchtung
LED Straßenbeleuchtung
Intelligente LED Beleuchtung
Gerne bin ich bezüglich der Aufteilung für Vorschläge und Anregungen offen.
Zielgruppe u.a. private Haushalte, Geschäftsführer, Einkäufer, Werkstattleiter
Aufgabenstellung
Logo ist bereits vorhanden.
Das Thema Energie soll ersichtlich sein. Ggf auch Energie- und CO2 Reduzierung.
Farbschema ist frei wählbar, sowie auch die Schriftart.
3 Gesichter für Kundenstimmen sollten mit vorhanden sein.
Das Logo darf auch gerne anders angeordnet werden z.B. Kopf des Fuchses links vor dem Text.

```html
<!DOCTYPE html>
<html lang="de">
<head>
<meta charset="utf-8">
<title>Brixowal – Energie und Kosten sparen</title>
<link href="https://fonts.googleapis.com/css2?family=Montserrat:wght@400;500;600;700&display=swap" rel="stylesheet">
<style>
  :root {
    --ink: #15222b;
    --night: #05070c;
    --yellow: #fdbf2d;
    --yellow-field: #e0ad38;
    --light: #f6f6f6;
    --white: #ffffff;
    --text-dark: #1a1a1a;
    --text-muted: #4a4a4a;
    --hairline: rgba(255,255,255,0.35);
  }
  * { margin: 0; padding: 0; box-sizing: border-box; }
  html, body { width: 1200px; height: 2754px; overflow: hidden; }
  body {
    position: relative;
    font-family: "Montserrat", sans-serif;
    background: var(--ink);
    color: var(--white);
  }
  .abs { position: absolute; }

  /* Hero */
  .hero-photo {
    position: absolute; left: 0; top: 0; width: 1200px; height: 674px;
    background:
      radial-gradient(ellipse 140px 60px at 340px 490px, rgba(255,214,140,0.55), transparent 70%),
      radial-gradient(ellipse 220px 90px at 600px 420px, rgba(230,170,80,0.35), transparent 70%),
      radial-gradient(ellipse 260px 110px at 820px 500px, rgba(230,160,70,0.3), transparent 70%),
      radial-gradient(ellipse 900px 300px at 650px 470px, rgba(70,85,110,0.75), transparent 75%),
      radial-gradient(ellipse 1000px 200px at 700px 210px, rgba(40,70,60,0.6), transparent 70%),
      linear-gradient(180deg, #020306 0%, #05080e 28%, #1b2536 55%, #2b3446 100%);
  }
  .hero-shade {
    position: absolute; left: 992px; top: 160px; width: 208px; height: 514px;
    background: rgba(0,0,0,0.25);
  }
  .brand {
    position: absolute; left: 106px; top: 24px;
    display: flex; align-items: center; gap: 10px;
    font-size: 24px; font-weight: 600; color: var(--white);
  }
  .brand-mark { width: 22px; height: 22px; background: var(--white); }
  .main-nav { position: absolute; top: 32px; font-size: 12px; font-weight: 500; }
  .main-nav a { position: absolute; color: var(--white); text-decoration: none; white-space: nowrap; }
  .header-rule { position: absolute; left: 99px; top: 79px; width: 1002px; height: 1px; background: var(--hairline); }
  .hero-title {
    position: absolute; left: 99px; top: 212px;
    font-size: 45px; font-weight: 700; line-height: 50px; letter-spacing: 0.3px;
  }
  .hero-link {
    position: absolute; left: 99px; top: 342px;
    display: flex; align-items: center; gap: 10px;
    font-size: 12px; font-weight: 700;
  }
  .hero-link::before { content: ""; width: 15px; height: 2px; background: var(--yellow); }
  .slider-control {
    position: absolute; left: 966px; top: 218px; width: 50px; height: 227px;
    background: var(--yellow); color: var(--text-dark);
    font-size: 9px; font-weight: 600; text-align: center;
  }
  .slider-control svg { position: absolute; left: 19px; }
  .slide-num { position: absolute; left: 0; width: 100%; }
  .slide-track { position: absolute; left: 24px; top: 82px; width: 1px; height: 70px; background: rgba(0,0,0,0.2); }
  .slide-track::before { content: ""; position: absolute; left: 0; top: 0; width: 1px; height: 40px; background: var(--text-dark); }

  /* Services */
  .service {
    position: absolute; padding: 0 26px;
    display: flex; align-items: flex-end;
    font-size: 13px; font-weight: 500; line-height: 14px; letter-spacing: 0.4px;
    color: var(--text-muted);
  }
  .service.light { background: var(--light); }
  .service.white { background: var(--white); }
  .service.active { background: var(--yellow); color: #3b2f10; }

  /* About */
  .section-title { position: absolute; font-size: 18px; font-weight: 700; }
  .about-text { position: absolute; left: 158px; top: 1086px; width: 310px; font-size: 11.5px; line-height: 19.5px; }
  .stat { position: absolute; top: 1066px; }
  .stat-label { font-size: 11px; font-weight: 700; }
  .stat-value { font-size: 54px; font-weight: 700; line-height: 60px; margin-top: 16px; }

  /* Testimonials */
  .portrait { position: absolute; top: 1491px; width: 201px; height: 201px; border-radius: 50%; }
  .quote { position: absolute; top: 1738px; width: 230px; font-size: 11.5px; line-height: 16px; }
  .quote cite { display: block; font-style: normal; margin-top: 24px; }

  /* Contact */
  .contact { position: absolute; left: 0; top: 2012px; width: 1200px; height: 549px; background: var(--yellow); color: var(--text-dark); }
  .contact-label { position: absolute; left: 158px; top: 114px; font-size: 14px; font-weight: 500; }
  .contact-rule { position: absolute; left: 158px; top: 143px; width: 885px; height: 1px; background: rgba(0,0,0,0.45); }
  .contact-title { position: absolute; left: 158px; top: 203px; font-size: 33px; font-weight: 700; line-height: 38px; }
  .field {
    position: absolute; background: var(--yellow-field);
    font-size: 9px; color: rgba(0,0,0,0.5); padding: 20px 13px 0;
  }
  .send { position: absolute; left: 953px; top: 414px; display: flex; align-items: center; gap: 22px; font-size: 13px; font-weight: 700; }

  /* Footer */
  .footer-brand { position: absolute; left: 158px; top: 2654px; display: flex; align-items: center; gap: 8px; font-size: 17px; font-weight: 600; }
  .footer-brand .brand-mark { width: 16px; height: 16px; }
  .footer-links { position: absolute; top: 2635px; font-size: 11.5px; line-height: 24px; list-style: none; }
  .footer-contact { position: absolute; top: 2641px; font-size: 11.5px; line-height: 17px; font-style: normal; }
</style>
</head>
<body>

  <header>
    <div class="hero-photo" role="img" aria-label="Nachtaufnahme der Erde aus dem All mit leuchtenden Städten"></div>
    <div class="hero-shade"></div>
    <div class="brand"><span class="brand-mark"></span>Brixowal</div>
    <nav class="main-nav">
      <a style="left:761px">Services</a>
      <a style="left:842px">About</a>
      <a style="left:910px">Contact</a>
    </nav>
    <svg class="abs" style="left:1044px;top:32px" width="16" height="16" viewBox="0 0 16 16" fill="none" stroke="#fff" stroke-width="1.4"><circle cx="6.5" cy="6.5" r="5.2"/><line x1="10.3" y1="10.3" x2="15" y2="15"/></svg>
    <svg class="abs" style="left:1085px;top:33px" width="16" height="13" viewBox="0 0 16 13" stroke="#fff" stroke-width="1.4"><line x1="0" y1="1" x2="16" y2="1"/><line x1="0" y1="6.5" x2="16" y2="6.5"/><line x1="0" y1="12" x2="16" y2="12"/></svg>
    <div class="header-rule"></div>
  </header>

  <section class="hero">
    <h1 class="hero-title">Energie und<br>Kosten sparen.</h1>
    <a class="hero-link">mehr erfahren</a>
    <div class="slider-control">
      <svg style="top:20px" width="12" height="12" viewBox="0 0 12 12" fill="none" stroke="#3b2f10" stroke-width="1.2"><polyline points="8,1 3,6 8,11"/></svg>
      <span class="slide-num" style="top:66px">01</span>
      <span class="slide-track"></span>
      <span class="slide-num" style="top:154px">04</span>
      <svg style="top:196px" width="12" height="12" viewBox="0 0 12 12" fill="none" stroke="#1a1a1a" stroke-width="1.4"><polyline points="4,1 9,6 4,11"/></svg>
    </div>
  </section>

  <section class="services">
    <a class="service light" style="left:99px;top:660px;width:373px;height:184px;padding-bottom:22px">Strom- und Gastarife<br>für Privatkunden</a>
    <a class="service active" style="left:472px;top:660px;width:394px;height:97px;padding-left:30px;padding-bottom:21px">Strom- und Gastarife<br>für Geschäftskunden</a>
    <a class="service white" style="left:866px;top:660px;width:235px;height:97px;align-items:center">LED Strassenbeleuchtung</a>
    <a class="service white" style="left:472px;top:757px;width:229px;height:87px;padding-left:30px;padding-bottom:22px">LED Hallenbeleuchtung</a>
    <a class="service light" style="left:701px;top:757px;width:400px;height:87px;padding-bottom:22px">Intelligente LED<br>Beleuchtung</a>
  </section>

  <section class="about">
    <h2 class="section-title" style="left:158px;top:1045px">Wer wir sind</h2>
    <p class="about-text">Lorem ipsum dolor sit amet, consetetur sadipscing elitr, sed diam nonumy eirmod tempor invidunt ut labore et dolore magna aliquyam erat, sed diam voluptua. At vero eos et accusam et justo duo dolores et ea rebum. Stet clita kasd gubergren, no sea takimata sanctus est Lorem ipsum dolor sit amet.</p>
    <div class="stat" style="left:587px"><div class="stat-label">Wichtige Zahl</div><div class="stat-value">12</div></div>
    <div class="stat" style="left:732px"><div class="stat-label">Wichtige Zahl</div><div class="stat-value">2000</div></div>
    <div class="stat" style="left:938px"><div class="stat-label">Wichtige Zahl</div><div class="stat-value">545</div></div>
  </section>

  <section class="testimonials">
    <h2 class="section-title" style="left:158px;top:1414px">Das sagen unsere Kunden</h2>
    <div class="portrait" style="left:158px;background:radial-gradient(circle at 50% 45%,#c9a58c,#b7a79b 55%,#7d6a60)" role="img" aria-label="Porträt eines lächelnden Kunden im hellen Sakko"></div>
    <div class="portrait" style="left:500px;background:radial-gradient(circle at 50% 45%,#7a4f3a,#b99583 55%,#d7cfc9)" role="img" aria-label="Porträt einer lächelnden Kundin im roten Oberteil"></div>
    <div class="portrait" style="left:842px;background:radial-gradient(circle at 50% 40%,#5a4a42,#2a2d33 55%,#15181d)" role="img" aria-label="Porträt eines Kunden im dunklen Anzug"></div>
    <blockquote class="quote" style="left:158px">"Lorem ipsum dolor sit amet, consetetur sadipscing elitr, sed diam nonumy eirmod tempor invidunt ut labore et."<cite>- Jon Doe, Doe AG</cite></blockquote>
    <blockquote class="quote" style="left:497px">"Lorem ipsum dolor sit amet, consetetur sadipscing elitr, sed diam nonumy eirmod tempor invidunt ut labore et."<cite style="margin-top:16px">&nbsp;- Jane Doe, Muster GmbH</cite></blockquote>
    <blockquote class="quote" style="left:847px;width:200px">"Lorem ipsum dolor sit amet, consetetur sadipscing elitr, sed diam nonumy eirmod tempor invidunt ut."<cite style="margin-top:16px">- Jon Doe, Energy AG</cite></blockquote>
  </section>

  <section class="contact">
    <div class="contact-label">Kontaktformular</div>
    <div class="contact-rule"></div>
    <h2 class="contact-title">Wie können wir<br>Ihnen helfen?</h2>
    <div class="field" style="left:484px;top:201px;width:164px;height:49px">Name</div>
    <div class="field" style="left:484px;top:263px;width:164px;height:49px">E-Mail</div>
    <div class="field" style="left:484px;top:325px;width:164px;height:49px">Telefon</div>
    <div class="field" style="left:667px;top:201px;width:375px;height:173px;padding-top:18px">Ihre Nachricht</div>
    <div class="send">Senden
      <svg width="18" height="16" viewBox="0 0 18 16"><path d="M0 0 L18 8 L0 16 L4 8 Z" fill="#1a1a1a"/></svg>
    </div>
  </section>

  <footer>
    <div class="footer-brand"><span class="brand-mark"></span>Brixowal</div>
    <ul class="footer-links" style="left:309px"><li>Services</li><li>About</li><li>Contact</li></ul>
    <ul class="footer-links" style="left:387px"><li>Impressum</li><li>AGB</li><li>Datenschutz</li></ul>
    <address class="footer-contact" style="left:806px">Max Muster<br>Musterstrasse 20<br>3000 Musterhausen</address>
    <address class="footer-contact" style="left:953px;top:2640px">info@brixowal.ch<br>031 555 48 20</address>
  </footer>

</body>
</html>
```